The Brambury Firm

We need a new design for our letterhead and envelopes. We are a personal injury and criminal defense firm so we need something modern and clean, but more on the professional/traditional side. Our new logo has two colors and is attached to the file so we need something that works well with those colors/matches the design. The following information needs to be on the letterhead:
Phone: (555) 314-7265
Fax: (555) 419-6032
Toll-Free: (555) 736-1149
Post Office Box 4273
Ashcombe, TQ 29458-4273
TQHarmClaimsDesk.example
PalmettoShieldCounsel.example

Target Market(s)

Clients, government agencies, other law firms

Industry/Entity Type

Legal

Font styles to use
Sans Serif
Other font styles liked:
• Arial

Colors

Designer to choose colors to be used in the design.

Requirements
Must have
• Must look professional and clean, modern
Nice to have
• I would like to see a design that works with the logo but does not distract from the content that will be printed on it
Should not have
• Too many colors or crazy designs.

```html
<!DOCTYPE html>
<html lang="en">
<head>
<meta charset="utf-8">
<title>The Brambury Firm — Stationery</title>
<link href="https://fonts.googleapis.com/css2?family=Open+Sans:wght@400;600&display=swap" rel="stylesheet">
<style>
  :root {
    --navy: #2b2d8e;
    --red: #d8292b;
    --paper: #ffffff;
    --backdrop: #e9e9ea;
    --ink-light: #ffffff;
  }
  * { box-sizing: border-box; margin: 0; padding: 0; }
  html, body { width: 1200px; height: 904px; overflow: hidden; }
  body {
    background: var(--backdrop);
    font-family: "Open Sans", Arial, sans-serif;
    position: relative;
  }
  .sheet {
    position: absolute;
    background: var(--paper);
    box-shadow: 0 2px 8px rgba(0,0,0,.18);
  }
  .letterhead { left: 88px; top: 134px; width: 493px; height: 697px; }
  .envelope-front { left: 612px; top: 273px; width: 508px; height: 255px; }
  .envelope-back { left: 612px; top: 565px; width: 508px; height: 255px; overflow: hidden; }

  .brand {
    position: absolute;
    display: flex;
    align-items: center;
    gap: 6px;
    font-weight: 600;
    font-size: 15px;
    letter-spacing: .3px;
    color: var(--navy);
    white-space: nowrap;
  }
  .brand-dot { width: 9px; height: 9px; border-radius: 50%; background: var(--red); }
  .letterhead .brand { left: 40px; top: 50px; }
  .envelope-front .brand { left: 27px; top: 38px; }
  .envelope-back .brand {
    left: 0; right: 0; top: 30px; justify-content: center;
    color: var(--ink-light); font-size: 12px;
  }

  .contact-band {
    position: absolute;
    left: 0;
    height: 40px;
    background: var(--navy);
    color: var(--ink-light);
    font-size: 7.4px;
    line-height: 10.2px;
  }
  .letterhead .contact-band { top: 637px; width: 440px; }
  .envelope-front .contact-band { top: 195px; width: 457px; }

  .contact-col { position: absolute; top: 8px; }
  .contact-line { display: flex; align-items: center; gap: 4px; white-space: nowrap; }
  .contact-line .spacer { width: 6px; }
  .contact-line svg { width: 6px; height: 6px; flex: none; }
  .divider { position: absolute; top: 4px; width: 1px; height: 32px; background: var(--ink-light); opacity: .8; }

  .letterhead .col-address { left: 40px; }
  .letterhead .div-1 { left: 151px; }
  .letterhead .col-phone { left: 163px; top: 3px; }
  .letterhead .div-2 { left: 240px; }
  .letterhead .col-web { left: 252px; }

  .envelope-front .col-address { left: 27px; }
  .envelope-front .div-1 { left: 138px; }
  .envelope-front .col-phone { left: 149px; top: 3px; }
  .envelope-front .div-2 { left: 225px; }
  .envelope-front .col-web { left: 238px; }

  .flap { position: absolute; left: 0; top: 0; width: 508px; height: 80px; }
  .flap path { fill: var(--navy); }
</style>
</head>
<body>

<svg width="0" height="0" style="position:absolute">
  <defs>
    <symbol id="icon-pin" viewBox="0 0 10 10"><path d="M5 0a3.5 3.5 0 0 0-3.5 3.5C1.5 6 5 10 5 10s3.5-4 3.5-6.5A3.5 3.5 0 0 0 5 0zm0 5a1.5 1.5 0 1 1 0-3 1.5 1.5 0 0 1 0 3z" fill="#d8292b"/></symbol>
    <symbol id="icon-phone" viewBox="0 0 10 10"><path d="M2 0.5 3.8 2.3 2.8 3.6c.7 1.5 2 2.8 3.6 3.6L7.7 6.2 9.5 8 8.3 9.5C4 9.3.7 6 .5 1.7z" fill="#d8292b"/></symbol>
    <symbol id="icon-fax" viewBox="0 0 10 10"><rect x="2.5" y="0.5" width="5" height="3" fill="#d8292b"/><rect x="0.5" y="4" width="9" height="5" rx="1" fill="#d8292b"/></symbol>
    <symbol id="icon-web" viewBox="0 0 10 10"><circle cx="5" cy="5" r="4.2" fill="none" stroke="#d8292b" stroke-width="1.3"/><path d="M1 5h8M5 1c-2 2.5-2 5.5 0 8M5 1c2 2.5 2 5.5 0 8" fill="none" stroke="#d8292b" stroke-width=".9"/></symbol>
  </defs>
</svg>

<section class="sheet letterhead" aria-label="Letterhead">
  <div class="brand"><span class="brand-dot"></span>The Brambury Firm</div>
  <footer class="contact-band">
    <div class="contact-col col-address">
      <div class="contact-line"><svg><use href="#icon-pin"/></svg>Post Office Box 4273</div>
      <div class="contact-line"><span class="spacer"></span>Ashcombe, TQ 29458-4273</div>
    </div>
    <span class="divider div-1"></span>
    <div class="contact-col col-phone">
      <div class="contact-line"><svg><use href="#icon-phone"/></svg>(555) 314-7265</div>
      <div class="contact-line"><svg><use href="#icon-fax"/></svg>(555) 419-6032</div>
      <div class="contact-line"><svg><use href="#icon-phone"/></svg>(555) 736-1149</div>
    </div>
    <span class="divider div-2"></span>
    <div class="contact-col col-web">
      <div class="contact-line"><svg><use href="#icon-web"/></svg>TQHarmClaimsDesk.example</div>
      <div class="contact-line"><svg><use href="#icon-web"/></svg>PalmettoShieldCounsel.example</div>
    </div>
  </footer>
</section>

<section class="sheet envelope-front" aria-label="Envelope front">
  <div class="brand"><span class="brand-dot"></span>The Brambury Firm</div>
  <footer class="contact-band">
    <div class="contact-col col-address">
      <div class="contact-line"><svg><use href="#icon-pin"/></svg>Post Office Box 4273</div>
      <div class="contact-line"><span class="spacer"></span>Ashcombe, TQ 29458-4273</div>
    </div>
    <span class="divider div-1"></span>
    <div class="contact-col col-phone">
      <div class="contact-line"><svg><use href="#icon-phone"/></svg>(555) 314-7265</div>
      <div class="contact-line"><svg><use href="#icon-fax"/></svg>(555) 419-6032</div>
      <div class="contact-line"><svg><use href="#icon-phone"/></svg>(555) 736-1149</div>
    </div>
    <span class="divider div-2"></span>
    <div class="contact-col col-web">
      <div class="contact-line"><svg><use href="#icon-web"/></svg>TQHarmClaimsDesk.example</div>
      <div class="contact-line"><svg><use href="#icon-web"/></svg>PalmettoShieldCounsel.example</div>
    </div>
  </footer>
</section>

<section class="sheet envelope-back" aria-label="Envelope back">
  <svg class="flap" viewBox="0 0 508 80" aria-hidden="true">
    <path d="M0 0H508V6C508 26 496 37 470 41L282 68Q254 73 226 68L38 41C12 37 0 26 0 6Z"/>
  </svg>
  <div class="brand">The Brambury Firm</div>
</section>

</body>
</html>
```